Anzeigengestaltung für Spezialist auf den drei Technologiefeldern Hydraulik, Prüfstandsbau und Laserschneiden
Zielgruppe
Die Friedrich Wolters GmbH ist Spezialist auf den drei Technologiefeldern Hydraulik, Prüfstandsbau und Laserschneiden. Wir vereinen drei Jahrzehnte Erfahrung im Bereich Hydraulik mit ständig aktualisiertem Fachwissen und entwickeln individuelle Lösungen, die exakt auf die Herausforderungen unserer Kunden zugeschnitten sind.
Aufgabenstellung
Die Anzeige soll eine wiederverwendbare (Text soll von uns in Zukunft bearbeitet werden können) Stellenanzeige werden, die unser modernes und attraktives Unternehmen in diversen Medien repräsentiert. Wir sind ein mitarbeiterfreundliches Familienunternehmen in 2. Generation. Dementsprechend sollte die Anzeige gestaltet sein.
Bilder und Texte dürfen auch von unserer Homepage verwendet werden. Wir sind für alles offen. lediglich unser Corporate Design sollte eingehalten werden. Dieses senden wir nach Auftragsvergabe zu.

```html
<!DOCTYPE html>
<html lang="de">
<head>
<meta charset="utf-8">
<title>Stellenanzeige – Friedrich Wolters GmbH</title>
<link href="https://fonts.googleapis.com/css2?family=Fira+Sans+Extra+Condensed:wght@400;500;600&family=Lexend+Exa:wght@400;600&display=swap" rel="stylesheet">
<style>
  :root {
    --navy: #0e3e66;
    --yellow: #f3c600;
    --ink: #222;
    --page: #f1f1f1;
    --paper: #ffffff;
    --photo-top: #eef1f4;
    --photo-bottom: #b9c3cc;
  }
  html, body {
    margin: 0; padding: 0;
    width: 1200px; height: 744px;
    overflow: hidden;
    background: var(--page);
  }
  .ad {
    position: absolute;
    left: 360px; top: 14px;
    width: 480px; height: 714px;
    background: var(--paper);
    border: 1px solid #cfd5da;
    box-sizing: border-box;
    display: flex; flex-direction: column;
    font-family: "Fira Sans Extra Condensed", "Arial Narrow", sans-serif;
    color: var(--ink);
  }
  .ad__headline {
    background: var(--navy);
    color: #fff;
    height: 52px;
    display: flex; align-items: center; justify-content: center;
    font-family: "Lexend Exa", sans-serif;
    font-size: 32px; letter-spacing: 0.5px;
    margin: 0; font-weight: 400;
  }
  .ad__headline strong { color: var(--yellow); font-weight: 600; }
  .ad__photo {
    height: 156px;
    background: linear-gradient(180deg, var(--photo-top), var(--photo-bottom));
  }
  .ad__position {
    background: var(--navy);
    color: #fff;
    height: 60px;
    margin: 0;
    display: flex; flex-direction: column; align-items: center; justify-content: center;
    font-size: 19px; font-weight: 400; line-height: 1.4;
  }
  .ad__body { padding: 10px 34px 0 34px; font-size: 11.5px; line-height: 1.4; flex: 1; }
  .ad__intro { color: var(--navy); font-size: 12.5px; font-weight: 500; margin: 0 0 16px; white-space: nowrap; }
  .ad__section-title { color: var(--navy); font-weight: 500; font-size: 10.5px; margin: 10px 0 4px; text-transform: uppercase; }
  .ad__list { margin: 0; padding-left: 12px; list-style: square; }
  .ad__contact { margin: 24px 0 5px; }
  .ad__contact em { color: var(--navy); font-style: normal; font-weight: 500; }
  .ad__mail { text-align: center; color: var(--navy); font-weight: 500; margin: 0; }
  .ad__mail .arrow { color: var(--yellow); font-weight: 600; }
  .ad__footer { display: flex; height: 46px; margin-bottom: 0; }
  .ad__brand {
    width: 155px; display: flex; align-items: center; justify-content: center; gap: 7px;
    color: var(--navy); font-size: 13px; font-weight: 500;
  }
  .ad__brand-dot { width: 14px; height: 14px; border-radius: 50%; background: var(--yellow); }
  .ad__address {
    flex: 1; background: var(--navy); color: #fff;
    display: flex; flex-direction: column; justify-content: center;
    padding-left: 8px; font-size: 10.5px; line-height: 1.35;
  }
  .ad__address b { font-weight: 500; }
</style>
</head>
<body>
<article class="ad">
  <h1 class="ad__headline">Wir suchen&nbsp;<strong>DICH!</strong></h1>
  <div class="ad__photo" role="img" aria-label="Foto: junges Team aus sieben Mitarbeitern, die lächelnd auf den Betrachter zeigen"></div>
  <h2 class="ad__position"><span>ELEKTRONIKER(IN) FÜR</span><span>BETRIEBSTECHNIK / MECHATRONIKER(IN)</span></h2>
  <div class="ad__body">
    <p class="ad__intro">Wir sind seit fast 30 Jahren Bestehen gemeinsam erfolgreich – willst DU dazu gehören?</p>
    <h3 class="ad__section-title">Dein Tätigkeitsbereich bei uns:</h3>
    <ul class="ad__list">
      <li>Aufbau von Schaltschränken nach Montage-/Stromlaufplänen</li>
      <li>Elektrischer Anschluss und mechanischer Aufbau von Prüfständen und Aggregaten</li>
      <li>Fehlersuche und Troubleshooting in unserer Werkstatt und vor Ort beim Kunden</li>
      <li>Eigenverantwortliche Inbetriebnahme von Hydraulikaggregaten und Schaltschränken</li>
    </ul>
    <h3 class="ad__section-title">Unsere Anforderungen an Dich:</h3>
    <ul class="ad__list">
      <li>Abgeschlossene elektrotechnische/mechatronische Ausbildung</li>
      <li>Mechanische Grundfähigkeiten</li>
      <li>Grundwissen der Hydraulik und Programmierkenntnisse in Vektron V7/Nexo und/oder Codaris und/oder LabSuite sind von Vorteil</li>
      <li>Strukturierte, selbständige und lösungsorientierte Arbeitsweise</li>
    </ul>
    <h3 class="ad__section-title">Wir bieten Dir:</h3>
    <ul class="ad__list">
      <li>Selbständige Tätigkeit in einem dynamischen Betätigungsfeld</li>
      <li>Abwechslungsreiche und interessante Aufgaben in einem innovativen Familienbetrieb</li>
      <li>Kurze Kommunikationswege durch eine flache Unternehmensstruktur</li>
      <li>Offenes Betriebsklima mit dynamischen Kollegen und Kolleginnen</li>
    </ul>
    <p class="ad__contact"><em>Interessiert? SUPER! Deine Ansprechpartnerin</em> Frau Katrin Wolters, freut sich schon Dich kennen zu lernen. Schicke am besten noch heute Deine Unterlagen (Anschreiben und Lebenslauf) an:</p>
    <p class="ad__mail"><span class="arrow">➔</span> JOBS@WOLTERS-TECHNIK.DE <span class="arrow">←</span></p>
  </div>
  <footer class="ad__footer">
    <div class="ad__brand"><span class="ad__brand-dot"></span>Friedrich Wolters</div>
    <div class="ad__address">
      <b>Friedrich Wolters GmbH – Lindenweg 14, 35781 Weilburg</b>
      <span>Telefon: 06471 55820-0 • Fax: 06471 55820-68 • www.wolters-technik.de</span>
    </div>
  </footer>
</article>
</body>
</html>
```